Looking for an Innovative Print Design (Service Directory)

We need a new design for our advertisement within a printed colour services directory.

We are a compensation law firm called Velbrook Compensation Lawyers. Feel free to take a browse of our website www.velbrooklegal.com.au to get an idea of what we do and the kind of firm we are.

We are in the process of redeveloping our website and as such, so please don't adhere to the design principles of the current site- impress us with your originality!

On top of any editable formats, your final submissions must include a .pdf copy.
The same design will need to be presented in two dimensions:

- 154mm x 118mm (B1/B2 Half Page);
- 175mm x 113mm (B4 Half Page).

[For more information refer to attached Pdf.]

We have attached for you a few examples of other firms' designs (Sample1,2,3). These are by no means good, or what we're after, it's just to provide you with an idea of what sort of advertisements go into the service directory.

Hi all,

We want to emphasise that a priority of the design is that it must look:
• Professional
• Sophisticated
Please do not hesitate to use completely different colour schemes to the ones that are on our website- as we have said, our website will change in the near future, so cohesion between the current project and the website is not necessary!

Thanks!

Thank you for your submissions so far. There are some great ideas hidden in there. 

An issue we are having is that most of you are conforming to the same understanding of what it should look like. Remember that there is NO NEED to be bound by the image of firm as is. That is, feel free to use a different colour logo.

For inspiration, we relate well to the design aesthetics of: http://www.tinfernstudio.co.uk/

Look forward to seeing your 'out of the box' submissions. 

Reason: We've received a large amount of fantastic designs. However, what we're really looking for is something original. Please feel free to think outside the box (the final design doesn't need to look like a print ad), and construct a design that is completely incongruous with our website! While we do appreciate a minimalistic design, we have yet to receive something that really grabs your attention with its visuals. We're not sure but this may or may not be achieved with a full colour design. Thanks for all your submissions- they all have some features that really click with us. We look forward to the next wave of submissions!

Target Market(s)

We have various target markets, including mainly families, elderly people, blue collar workers.

These are individuals who are looking for assistance. They feel helpless or wronged.

Keep in mind that the people accessing these are those who prefer going to a printed directory rather than using a google search.

Industry/Entity Type

Law Firm

Font styles to use
Serif
Sans Serif

Requirements
Must have
• - Our name 'Velbrook Compensation Lawyers'
- Our logo (attached as logo.eps, logo.png, and logo.tif)
- Must include phone number as 1300 XXX XXX (this must be prominent)
- Must include the following service areas in these words: Motor vehicle claims, medical claims, superannuation claims, Workplace claims, negligence claims
- Our email address: info@velbrooklegal.com.au
- Our website address: www.velbrooklegal.com.au
- The following catchphrases: '98% success rate', and 'No win no fee' in those words
- Our location '412 Carvel Lane, Smithville, SYDNEY'
- For sizing dimensions, we need one in 154mm x 118mm and also a design in 175mm x 113mm (B4 Half Page) [refer to pdf attached]
Nice to have
• - Text indicating free initial consulatation
- Professional colour scheme
- As our website will be changed, do not worry about making the advertisement cohesive with our website design
- We want the design to be modern, but still professional
- Clean typeface
- No gradient colour scheme
- When designing, if you are looking to place more text onto the advertisement, these may be some considerations (feel free to change the wording): Accredited specialists, home and hospital visits

```html
<!DOCTYPE html>
<html lang="en">
<head>
<meta charset="utf-8">
<title>Velbrook Compensation Lawyers – Directory Advertisements</title>
<link rel="stylesheet" href="https://fonts.googleapis.com/css2?family=Tinos:wght@400;700&display=swap">
<style>
  :root {
    --stage: #2b2d2f;
    --paper: #ffffff;
    --brand-blue: #2f9bd6;
    --brand-orange: #f15a0f;
    --soft-peach: #fcdcca;
    --ink: #333333;
    --photo-light: #c9d6dc;
    --photo-dark: #3a4656;
  }
  * { margin: 0; padding: 0; box-sizing: border-box; }
  html, body {
    width: 1000px;
    height: 1200px;
    overflow: hidden;
    background: var(--stage);
  }
  body { position: relative; font-family: "Tinos", "Times New Roman", serif; }
  .ad { position: absolute; display: block; background: var(--paper); }
  .ad--half-b1 { left: 209px; top: 106px; width: 582px; height: 448px; }
  .ad--half-b4 { left: 139px; top: 644px; width: 719px; height: 466px; }

  .fill-blue { fill: var(--brand-blue); }
  .fill-orange { fill: var(--brand-orange); }
  .fill-peach { fill: var(--soft-peach); }
  .fill-white { fill: var(--paper); }

  .ad text { font-family: "Tinos", "Times New Roman", serif; }
  .brand-name { fill: var(--paper); font-weight: 400; letter-spacing: 0.5px; }
  .phone { fill: var(--paper); font-weight: 700; }
  .section-title { fill: var(--brand-blue); font-weight: 700; }
  .service { fill: var(--ink); letter-spacing: 0.8px; word-spacing: 3px; }
  .contact-line { fill: var(--ink); }
  .contact-line--light { fill: var(--paper); }
  .headline-name { fill: var(--brand-orange); font-weight: 700; }
  .headline-sub { fill: var(--ink); letter-spacing: 0.4px; word-spacing: 2px; }
  .claim { font-weight: 700; }
  .claim-orange { fill: var(--brand-orange); }
  .claim-blue { fill: var(--brand-blue); }
  .address-street { fill: var(--paper); font-weight: 700; letter-spacing: 0.3px; }
  .address-city { fill: var(--paper); letter-spacing: 0.6px; }
  .icon-stroke { fill: none; stroke: var(--brand-orange); stroke-width: 1.4; }
  .icon-stroke--light { fill: none; stroke: var(--paper); stroke-width: 1.3; }
</style>
</head>
<body>

<!-- 154mm x 118mm half page -->
<svg class="ad ad--half-b1" viewBox="0 0 582 448" width="582" height="448" xmlns="http://www.w3.org/2000/svg">
  <defs>
    <clipPath id="b1-bounds"><rect width="582" height="448"/></clipPath>
    <linearGradient id="b1-photo-tone" x1="0" x2="1" y1="0" y2="0">
      <stop offset="0" stop-color="var(--photo-light)"/>
      <stop offset="1" stop-color="var(--photo-dark)"/>
    </linearGradient>
  </defs>
  <g clip-path="url(#b1-bounds)">
    <circle class="fill-peach" cx="452" cy="272" r="200"/>
  </g>

  <polygon class="fill-blue" points="0,0 582,0 582,62 298,62 278,82 0,82"/>
  <polygon class="fill-orange" points="302,66 582,66 582,80 288,80"/>

  <polygon class="fill-blue" points="0,394 282,394 266,410 0,410"/>
  <polygon class="fill-orange" points="0,414 272,414 296,392 582,392 582,448 0,448"/>

  <rect class="fill-orange" x="0" y="114" width="32" height="24"/>
  <rect class="fill-blue" x="553" y="117" width="29" height="23"/>

  <circle class="fill-orange" cx="57" cy="42" r="17"/>
  <text class="brand-name" x="84" y="48" font-size="17">Velbrook Compensation Lawyers</text>

  <text class="phone" x="553" y="49" font-size="31" text-anchor="end">1300 482 317</text>

  <text class="section-title" x="37" y="137" font-size="25">Our Service</text>

  <g class="service-list">
    <circle class="fill-orange" cx="43" cy="162" r="7"/>
    <text class="service" x="57" y="167" font-size="15.5">Motor vehicle claims</text>
    <circle class="fill-orange" cx="43" cy="204" r="7"/>
    <text class="service" x="57" y="209" font-size="15.5">Medical claims</text>
    <circle class="fill-orange" cx="43" cy="247" r="7"/>
    <text class="service" x="57" y="252" font-size="15.5">Superannuation claims</text>
    <circle class="fill-orange" cx="43" cy="289" r="7"/>
    <text class="service" x="57" y="294" font-size="15.5">Workplace claims</text>
    <circle class="fill-orange" cx="43" cy="332" r="7"/>
    <text class="service" x="57" y="337" font-size="15.5">Negligence claims</text>
  </g>

  <g class="email-icon">
    <rect class="icon-stroke" x="36" y="367" width="14" height="10"/>
    <polyline class="icon-stroke" points="36,367 43,373 50,367"/>
  </g>
  <text class="contact-line" x="56" y="377" font-size="11.5">info@velbrooklegal.com.au</text>

  <text class="headline-name" x="551" y="140" font-size="36" text-anchor="end">Velbrook</text>
  <text class="headline-sub" x="552" y="164" font-size="17" text-anchor="end">Compensation Lawyers</text>
  <text class="claim" x="552" y="199" text-anchor="end"><tspan class="claim-orange" font-size="31">98%</tspan><tspan class="claim-blue" font-size="26"> success rate</tspan></text>
  <text class="claim" x="552" y="242" font-size="26" text-anchor="end"><tspan class="claim-blue">No </tspan><tspan class="claim-orange">win no </tspan><tspan class="claim-blue">fee</tspan></text>

  <g role="img" aria-label="Photograph of a lawyer in a suit consulting with a client across a desk">
    <rect x="356" y="274" width="196" height="103" fill="url(#b1-photo-tone)"/>
  </g>

  <text class="address-street" x="552" y="415" font-size="15" text-anchor="end">412 Carvel Lane</text>
  <text class="address-city" x="552" y="434" font-size="12.5" text-anchor="end">Smithville, SYDNEY</text>

  <g class="web-icon">
    <circle class="icon-stroke--light" cx="43" cy="429" r="7"/>
    <line class="icon-stroke--light" x1="36" y1="429" x2="50" y2="429"/>
    <ellipse class="icon-stroke--light" cx="43" cy="429" rx="3" ry="7"/>
  </g>
  <text class="contact-line--light" x="55" y="433" font-size="12">www.velbrooklegal.com.au</text>
</svg>

<!-- 175mm x 113mm B4 half page -->
<svg class="ad ad--half-b4" viewBox="0 0 719 466" width="719" height="466" xmlns="http://www.w3.org/2000/svg">
  <defs>
    <clipPath id="b4-bounds"><rect width="719" height="466"/></clipPath>
    <linearGradient id="b4-photo-tone" x1="0" x2="1" y1="0" y2="0">
      <stop offset="0" stop-color="var(--photo-light)"/>
      <stop offset="1" stop-color="var(--photo-dark)"/>
    </linearGradient>
  </defs>
  <g clip-path="url(#b4-bounds)">
    <circle class="fill-peach" cx="562" cy="286" r="230"/>
  </g>

  <polygon class="fill-blue" points="0,0 719,0 719,66 424,66 400,89 0,89"/>
  <polygon class="fill-orange" points="430,70 719,70 719,87 412,87"/>

  <polygon class="fill-blue" points="0,408 332,408 314,426 0,426"/>
  <polygon class="fill-orange" points="0,430 318,430 342,408 719,408 719,466 0,466"/>

  <rect class="fill-orange" x="0" y="124" width="37" height="26"/>
  <rect class="fill-blue" x="687" y="128" width="32" height="33"/>

  <circle class="fill-orange" cx="65" cy="48" r="24"/>
  <text class="brand-name" x="100" y="55" font-size="20">Velbrook Compensation Lawyers</text>

  <text class="phone" x="682" y="54" font-size="37" text-anchor="end">1300 482 317</text>

  <text class="section-title" x="41" y="148" font-size="27">Our Service</text>

  <g class="service-list">
    <circle class="fill-orange" cx="47" cy="176" r="8"/>
    <text class="service" x="64" y="182" font-size="16.5">Motor vehicle claims</text>
    <circle class="fill-orange" cx="47" cy="220" r="8"/>
    <text class="service" x="64" y="226" font-size="16.5">Medical claims</text>
    <circle class="fill-orange" cx="47" cy="264" r="8"/>
    <text class="service" x="64" y="270" font-size="16.5">Superannuation claims</text>
    <circle class="fill-orange" cx="47" cy="307" r="8"/>
    <text class="service" x="64" y="313" font-size="16.5">Workplace claims</text>
    <circle class="fill-orange" cx="47" cy="351" r="8"/>
    <text class="service" x="64" y="357" font-size="16.5">Negligence claims</text>
  </g>

  <g class="email-icon">
    <rect class="icon-stroke" x="39" y="385" width="16" height="11"/>
    <polyline class="icon-stroke" points="39,385 47,392 55,385"/>
  </g>
  <text class="contact-line" x="62" y="395" font-size="11.5">info@velbrooklegal.com.au</text>

  <text class="headline-name" x="685" y="156" font-size="40" text-anchor="end">Velbrook</text>
  <text class="headline-sub" x="685" y="182" font-size="17" text-anchor="end">Compensation Lawyers</text>
  <text class="claim" x="685" y="222" text-anchor="end"><tspan class="claim-orange" font-size="33">98%</tspan><tspan class="claim-blue" font-size="28"> success rate</tspan></text>
  <text class="claim" x="685" y="262" font-size="29" text-anchor="end"><tspan class="claim-blue">No </tspan><tspan class="claim-orange">win no </tspan><tspan class="claim-blue">fee</tspan></text>

  <g role="img" aria-label="Photograph of a lawyer in a suit consulting with a client across a desk">
    <rect x="473" y="284" width="213" height="112" fill="url(#b4-photo-tone)"/>
  </g>

  <text class="address-street" x="685" y="431" font-size="15.5" text-anchor="end">412 Carvel Lane</text>
  <text class="address-city" x="685" y="453" font-size="13" text-anchor="end">Smithville, SYDNEY</text>

  <g class="web-icon">
    <circle class="icon-stroke--light" cx="46" cy="446" r="8"/>
    <line class="icon-stroke--light" x1="38" y1="446" x2="54" y2="446"/>
    <ellipse class="icon-stroke--light" cx="46" cy="446" rx="3.5" ry="8"/>
  </g>
  <text class="contact-line--light" x="59" y="450" font-size="12">www.velbrooklegal.com.au</text>
</svg>

</body>
</html>
```